Junk Removal business needs a small billboard design

We are looking to have a billboard design made that will pop out to motorist passing by. The sign will be 6 foot wide by 4 foot tall. We would like it to say:SHOW US YOUR JUNK! 614-287-3391 BIG OR SMALL... WE HAUL IT ALL VICTORY JUNK REMOVALWe have provided a rough draft sketch photo of how large we would want the text. Preferably we want the text to be very large and use up most of the space and to be seen from far away. Also, there are example photos of the green background color and text colors we would like to incorporate into the design. We would like to add our company logo (Files attached) on the billboard too. Next to the phone number we would like to add the camera icon (example photos attached) Thank you in advance for all your hard work!

Font styles to use
Serif
Sans Serif

Requirements
Must have
• Large font that is easy to read from far
• Company name must be large
Nice to have
• Bright and pop out to passing by motorist.

```html
<!DOCTYPE html>
<html lang="en">
<head>
<meta charset="utf-8">
<title>Mapleholt Junk Removal Billboard</title>
<link rel="stylesheet" href="https://fonts.googleapis.com/css2?family=Montserrat:wght@700;800;900&display=swap">
<style>
  :root {
    --backdrop: #a3a3a3;
    --sign-green: #8fbb45;
    --frame-line: #f4f8ec;
    --ink: #111111;
    --paper: #ffffff;
    --ribbon: #e8532f;
    --camera-body: #d9663a;
    --camera-top: #6f8f9b;
    --logo-disc: #6f6a4c;
  }
  * { margin: 0; padding: 0; box-sizing: border-box; }
  html, body {
    width: 1200px; height: 1000px; overflow: hidden;
    background: var(--backdrop);
    font-family: "Montserrat", Arial, sans-serif;
  }
  .billboard {
    position: absolute; left: 83px; top: 155px;
    width: 1034px; height: 688px;
    background: var(--paper);
  }
  .billboard__panel {
    position: absolute; left: 0; top: 0;
    width: 1034px; height: 530px;
    background: var(--sign-green);
  }
  .billboard__frame {
    position: absolute; left: 17px; top: 15px;
    width: 1000px; height: 498px;
    border: 2px solid var(--frame-line);
  }
  .headline-lead {
    position: absolute; left: 0; top: 36px; width: 100%;
    text-align: center; color: var(--paper);
    font-weight: 700; font-size: 80px; line-height: 1;
    letter-spacing: -1px;
  }
  .headline-main {
    position: absolute; left: 40px; top: 100px;
    overflow: visible;
  }
  .phone {
    position: absolute; left: 137px; top: 340px;
    display: flex; align-items: center; gap: 22px;
  }
  .phone__number {
    color: var(--ink); font-weight: 800; font-size: 88px;
    line-height: 1; letter-spacing: -1px;
  }
  .tagline {
    position: absolute; left: 112px; top: 435px;
  }
  .tagline__text {
    font-family: "Montserrat", Arial, sans-serif;
    font-weight: 800; font-size: 43px; fill: var(--paper);
  }
  .company {
    position: absolute; left: 0; top: 530px; width: 100%; height: 158px;
  }
  .company__mark {
    position: absolute; left: 90px; top: -8px;
    width: 150px; height: 150px; border-radius: 50%;
    background: var(--logo-disc);
  }
  .company__name {
    position: absolute; left: 292px; top: 56px;
    color: var(--ink); font-weight: 800; font-size: 43px;
    line-height: 1; white-space: nowrap;
  }
</style>
</head>
<body>
  <main class="billboard">
    <section class="billboard__panel">
      <div class="billboard__frame"></div>
      <p class="headline-lead">SHOW US YOUR</p>
      <svg class="headline-main" width="950" height="240" viewBox="0 0 950 240" aria-label="JUNK !">
        <text x="18" y="222" textLength="912" lengthAdjust="spacingAndGlyphs"
              font-family="Montserrat, Arial, sans-serif" font-weight="900" font-size="290"
              fill="#ffffff" stroke="#111111" stroke-width="16" stroke-linejoin="round"
              paint-order="stroke">JUNK !</text>
      </svg>
      <div class="phone">
        <svg class="phone__icon" width="98" height="74" viewBox="0 0 98 74" aria-hidden="true">
          <rect x="4" y="10" width="90" height="60" rx="8" fill="var(--camera-body)" stroke="#111" stroke-width="4"/>
          <rect x="4" y="10" width="90" height="18" rx="6" fill="var(--camera-top)" stroke="#111" stroke-width="4"/>
          <rect x="14" y="2" width="20" height="10" rx="2" fill="#111"/>
          <rect x="76" y="14" width="10" height="8" rx="1" fill="#fff"/>
          <circle cx="49" cy="42" r="22" fill="#ddd" stroke="#111" stroke-width="4"/>
          <circle cx="49" cy="42" r="13" fill="#444"/>
          <circle cx="44" cy="37" r="4" fill="#fff"/>
        </svg>
        <span class="phone__number">614-287-3391</span>
      </div>
      <svg class="tagline" width="810" height="58" viewBox="0 0 810 58">
        <polygon points="0,0 810,0 794,29 810,58 0,58 16,29" fill="var(--ribbon)"/>
        <text class="tagline__text" x="405" y="44" text-anchor="middle">BIG OR SMALL...WE HAUL IT ALL</text>
      </svg>
    </section>
    <section class="company">
      <div class="company__mark"></div>
      <h1 class="company__name">MAPLEHOLT JUNK REMOVAL</h1>
    </section>
  </main>
</body>
</html>
```